Fatigued and Overloaded by COVID Messages? We need original illustrations to show that.

Everywhere you look there are messages about COVID. That is leading many people to feel fatigued and overloaded by the messages.

We surveyed U.S. adults March 20th - 24th, 2020 and measured message fatigue, information overload, perceived repetition, and perceived exaggeration. Here is how participants responded:

When it comes to coronavirus . . .
55% feel exhausted by all the messages.
54% feel overloaded by the amount of information.
51% feel that the messages are repetitive.
47% feel like messages exaggerate how bad it is.

In other words, almost half of U.S. adults show signs of message fatigue, information overload, perceived message repetition, and perceived message exaggeration.

We will continue to survey 400 adults every week for the next 16 weeks. Each time we will measure message fatigue, information overload, perceived repetition, and perceived exaggeration. We expect that it will increase over time.

What are we looking for? We need innovative and original illustrations that attempt to communicate these findings. The illustrations would visualize message fatigue, information overload, perceived message repetition, and perceived message exaggeration.

What sort of visual are we looking for? Our preference is for an original illustration (or set of illustrations). Our preference is for creative and powerful illustrations, but we are also open to the creative and well-executed infographics.

We need these images fast . We will award monetary prizes to the 3 best designs. If we like more than that, then we might purchase more (e.g., in past contests, we have purchased as many as 30 designs).

What we will need:
(1) The illustrations must be original and we will need the photoshop and/or illustrator files for all artwork. (By original, we mean that the illustrations are 100% created by you. Our organization requires that we utilize only original illustrated work. We have had issues with free imagery being pirated and reposted as free. We sidestep that issue by just having everything created.)

(2) The illustration should say, somewhere: "Based on a survey of 400 U.S. adults conducted March 20 - 24th, 2020."

(3) We will have almost 4 months worth of data by the time this is done. In other words, the illustrations might be able to help us present that weekly data.

(4) We have conducted other Artvendo projects. It might be helpful to examine designs we liked in the past. For example, here is another COVID project we just finished:

https://jobs.artvendo-example.com/job/5162048

Target Market(s)

U.S. adults

Requirements
Must have
• Original illustrations. Mobile friendly design. People will view this on their smartphones.
Nice to have
• A design that we can use to communicate the data across time.

```html
<!DOCTYPE html>
<html lang="en">
<head>
<meta charset="UTF-8">
<title>When It Comes To Coronavirus – Message Fatigue Survey</title>
<link rel="stylesheet" href="https://fonts.googleapis.com/css2?family=Montserrat:wght@500;600;700;800&family=Oswald:wght@400&display=swap">
<style>
  :root {
    --purple: #652d90;
    --lavender: #8677d6;
    --track: #e6e1f3;
    --virus-tone: #c98be9;
    --virus-soft: #f1e4fa;
    --white: #ffffff;
    --ink: #1a1a1a;
    --icon-fill: #b9c4e6;
  }
  * { margin: 0; padding: 0; box-sizing: border-box; }
  html, body { width: 750px; height: 1200px; overflow: hidden; background: var(--white); }
  .poster {
    position: relative; width: 750px; height: 1200px; overflow: hidden;
    background: var(--white); font-family: 'Montserrat', sans-serif; color: var(--ink);
  }
  .top-band { position: absolute; left: 0; top: 0; width: 750px; height: 93px; background: var(--purple); }
  .kicker {
    position: absolute; left: 117px; top: 56px; width: 516px; height: 62px;
    background: var(--lavender); color: var(--white);
    font-weight: 700; font-size: 23px; letter-spacing: 0.2px;
    display: flex; align-items: center; justify-content: center;
  }
  .virus-field {
    position: absolute; left: 0; top: 118px; width: 750px; height: 420px;
    background:
      radial-gradient(circle at 14% 14%, var(--virus-tone) 0 55px, transparent 58px),
      radial-gradient(circle at 45% 24%, var(--virus-tone) 0 42px, transparent 45px),
      radial-gradient(circle at 73% 14%, var(--virus-tone) 0 50px, transparent 53px),
      radial-gradient(circle at 16% 88%, var(--virus-tone) 0 58px, transparent 61px),
      radial-gradient(circle at 55% 82%, var(--virus-tone) 0 52px, transparent 55px),
      radial-gradient(circle at 87% 85%, var(--virus-tone) 0 36px, transparent 39px),
      radial-gradient(ellipse at 50% 50%, var(--virus-soft), transparent 75%);
    opacity: 0.75;
  }
  .headline-shadow { position: absolute; left: 62px; top: 236px; width: 623px; height: 201px; background: var(--lavender); }
  .headline {
    position: absolute; left: 52px; top: 208px; width: 623px; height: 202px;
    background: var(--purple); color: var(--white);
    font-weight: 500; font-size: 43px; line-height: 53px; text-align: center;
    display: flex; align-items: center; justify-content: center; letter-spacing: 0.5px;
  }
  .results { position: absolute; left: 41px; top: 540px; width: 630px; }
  .result { position: relative; height: 81px; }
  .result-label {
    display: flex; justify-content: space-between; align-items: baseline;
    font-weight: 500; font-size: 23px; height: 42px; line-height: 36px;
  }
  .result-bar { width: 622px; height: 31px; background: var(--track); }
  .result-fill { height: 100%; background: var(--purple); }
  .prevention {
    position: absolute; left: 0; top: 954px; width: 750px; height: 246px; background: var(--purple);
  }
  .prevention-tab {
    position: absolute; left: 74px; top: -14px; width: 166px; height: 37px; background: var(--white);
    color: var(--purple); font-family: 'Oswald', sans-serif; font-size: 27px;
    display: flex; align-items: center; justify-content: center; line-height: 1;
  }
  .tip { position: absolute; top: 31px; width: 150px; margin-left: -75px; text-align: center; }
  .tip-icon {
    width: 112px; height: 112px; border-radius: 50%; margin: 0 auto;
    background: radial-gradient(circle at 50% 55%, var(--icon-fill) 0 30%, var(--white) 62%);
  }
  .tip-caption {
    margin-top: 14px; color: var(--white); font-weight: 800; font-size: 10px; line-height: 12.5px;
  }
  .footnote {
    position: absolute; left: 0; top: 210px; width: 750px; text-align: center;
    color: var(--white); font-weight: 500; font-size: 14px; letter-spacing: 0.2px;
  }
</style>
</head>
<body>
<div class="poster">
  <div class="top-band"></div>
  <div class="virus-field" role="img" aria-label="Scattered purple coronavirus particle illustrations"></div>
  <div class="kicker">WHEN IT COMES TO CORONAVIRUS</div>

  <div class="headline-shadow"></div>
  <h1 class="headline">SURVEY 400 ADULTS<br>EVERY WEEK FOR THE<br>NEXT 16 WEEKS</h1>

  <section class="results">
    <div class="result">
      <div class="result-label"><span>Exhausted by all the messages.</span><span>55%</span></div>
      <div class="result-bar"><div class="result-fill" style="width:59.3%"></div></div>
    </div>
    <div class="result">
      <div class="result-label"><span>Overloaded by the amount of information.</span><span>54%</span></div>
      <div class="result-bar"><div class="result-fill" style="width:55%"></div></div>
    </div>
    <div class="result">
      <div class="result-label"><span>The messages are repetitive.</span><span>51%</span></div>
      <div class="result-bar"><div class="result-fill" style="width:50%"></div></div>
    </div>
    <div class="result">
      <div class="result-label"><span>&nbsp;Messages exaggerate how bad it is.</span><span>47%</span></div>
      <div class="result-bar"><div class="result-fill" style="width:41.4%"></div></div>
    </div>
  </section>

  <section class="prevention">
    <div class="prevention-tab">PREVENTION</div>
    <div class="tip" style="left:133px">
      <div class="tip-icon" role="img" aria-label="Illustration of hands being washed with soap"></div>
      <p class="tip-caption">WASH YOUR<br>HANDS OFTEN</p>
    </div>
    <div class="tip" style="left:296px">
      <div class="tip-icon" role="img" aria-label="Illustration of a face mask"></div>
      <p class="tip-caption">WEAR A<br>FACE MASK</p>
    </div>
    <div class="tip" style="left:457px">
      <div class="tip-icon" role="img" aria-label="Illustration of a handshake crossed out"></div>
      <p class="tip-caption">AVOID CONTACT<br>WITH SICK PEOPLE</p>
    </div>
    <div class="tip" style="left:618px">
      <div class="tip-icon" role="img" aria-label="Illustration of a person covering a sneeze"></div>
      <p class="tip-caption">ALWAYS COVER YOUR<br>COUGH OR SNEEZE</p>
    </div>
    <p class="footnote">"BASED ON A SURVEY OF 400 U.S. ADULTS CONDUCTED MARCH 20 - 24TH, 2020</p>
  </section>
</div>
</body>
</html>
```